Flyer Design Project - Brightwell Fitness

I am looking for a flyer to distribute to multiple locations and target markets. It is for an Brightwell Fitness.
Special Promo (Biggest thing to highlight)
"Summer is FREE"
Need to have "When you Join Now"
Smaller details: Some Restrictions Apply
Need Brightwell Fitness Logo
24-Hour Access
Some photo to highlight a workout preferably a female as we tend to be a little more female than male.
Please see the attached files for the logo and a sample mailer we have done in the past. Color scheme of purple is needed.
Can examples be made to fit on a 5.47" Wide Flyer by 4.21" Tall.
Single Sided Flyer
Industry/Entity Type
Fitness
Look and feel
Each slider illustrates characteristics of the customer's brand and the style your logo design should communicate.

```html
<!DOCTYPE html>
<html lang="en">
<head>
<meta charset="utf-8">
<title>Brightwell Fitness – Summer Promo Flyer</title>
<link rel="stylesheet" href="https://fonts.googleapis.com/css2?family=Arvo:wght@700&family=Nunito:wght@900&family=Arimo:ital,wght@0,400;0,700;1,400&display=swap">
<style>
  :root {
    --backdrop: #e6e6e8;
    --purple: #6a2a8f;
    --purple-deep: #4f1f78;
    --purple-band: #7a2d92;
    --green-light: #8fd14a;
    --green: #3cb33f;
    --green-dark: #1f8f3a;
    --ink: #1c1c1c;
    --white: #ffffff;
    --silver: #c9ccd3;
  }
  * { margin: 0; padding: 0; box-sizing: border-box; }
  html, body { width: 1200px; height: 945px; overflow: hidden; }
  body { background: var(--backdrop); position: relative; }

  .flyer {
    position: absolute; left: 30px; top: 35px;
    width: 1140px; height: 875px;
    overflow: hidden; background: var(--white);
  }
  .flyer__photo {
    position: absolute; inset: 0;
    background:
      radial-gradient(ellipse 32% 45% at 82% 38%, rgba(214,160,130,.75), rgba(214,160,130,0) 70%),
      radial-gradient(ellipse 22% 30% at 48% 30%, rgba(205,165,140,.55), rgba(205,165,140,0) 70%),
      radial-gradient(ellipse 20% 30% at 98% 45%, rgba(160,70,160,.55), rgba(160,70,160,0) 70%),
      radial-gradient(ellipse 30% 40% at 20% 70%, rgba(90,100,120,.35), rgba(90,100,120,0) 70%),
      linear-gradient(120deg, #f3f6f8 0%, #e4e9ee 45%, #efe9e6 70%, #e8dcd6 100%);
  }
  .flyer__headline-glow {
    position: absolute; left: -60px; top: -120px;
    width: 960px; height: 320px; border-radius: 50%;
    background: rgba(255,255,255,.72);
  }
  .headline {
    position: absolute; left: 57px; top: 48px;
    font-family: "Arvo", Georgia, serif; font-weight: 700;
    font-size: 86px; line-height: 1;
    background: linear-gradient(180deg, var(--green-light), var(--green) 55%, var(--green-dark));
    -webkit-background-clip: text; background-clip: text; color: transparent;
  }
  .offer {
    position: absolute; left: 60px; top: 238px;
    font-family: "Nunito", Arial, sans-serif; font-weight: 900;
    color: var(--purple);
    text-shadow: 0 0 3px #fff, 2px 2px 0 #fff, -2px -2px 0 #fff, 2px -2px 0 #fff, -2px 2px 0 #fff;
  }
  .offer__lead { font-size: 68px; line-height: 1; }
  .offer__free { font-size: 84px; line-height: 1.05; margin-top: 6px; }
  .offer__note {
    position: absolute; left: 111px; top: 462px;
    font-family: "Arimo", Arial, sans-serif; font-weight: 700;
    font-size: 39px; color: var(--ink); letter-spacing: -.5px;
  }

  .band { position: absolute; left: 0; bottom: 0; width: 1140px; height: 160px; }

  .brand {
    position: absolute; left: 119px; top: 667px;
    width: 450px; height: 118px;
    background: var(--white); border-radius: 12px;
    display: flex; align-items: center; gap: 18px; padding: 0 26px;
    box-shadow: 0 2px 6px rgba(0,0,0,.2);
  }
  .brand__dot { width: 46px; height: 46px; border-radius: 50%; background: var(--purple); flex: none; }
  .brand__name {
    font-family: "Nunito", Arial, sans-serif; font-weight: 900;
    font-size: 40px; line-height: .98; color: var(--purple-deep); text-transform: uppercase;
  }

  .web {
    position: absolute; left: 136px; top: 818px;
    font-family: "Arimo", Arial, sans-serif; font-size: 30px;
    letter-spacing: .14em; color: var(--white);
  }
  .fine-print {
    position: absolute; right: 40px; top: 834px;
    font-family: "Arimo", Arial, sans-serif; font-style: italic;
    font-size: 22px; color: var(--white);
  }

  .badge { position: absolute; left: 845px; top: 528px; width: 268px; height: 268px; }
  .badge__text {
    position: absolute; inset: 0;
    display: flex; flex-direction: column; align-items: center; justify-content: center;
    text-align: center; padding-top: 4px;
  }
  .badge__num {
    font-family: "Nunito", Arial, sans-serif; font-weight: 900;
    font-size: 100px; line-height: .9; color: var(--purple);
    text-shadow: 2px 2px 0 #fff, -2px -2px 0 #fff, 2px -2px 0 #fff, -2px 2px 0 #fff;
  }
  .badge__label {
    font-family: "Arimo", Arial, sans-serif; font-weight: 700;
    font-size: 40px; line-height: 1.02; color: var(--white);
  }
</style>
</head>
<body>
  <main class="flyer">
    <div class="flyer__photo" role="img" aria-label="Photo of a smiling woman and other members working out on exercise bikes in a bright gym"></div>
    <div class="flyer__headline-glow"></div>

    <h1 class="headline">Special Promo</h1>

    <div class="offer">
      <p class="offer__lead">Summer is</p>
      <p class="offer__free">FREE</p>
    </div>
    <p class="offer__note">When you join now</p>

    <svg class="band" viewBox="0 0 1140 160" preserveAspectRatio="none" aria-hidden="true">
      <defs>
        <linearGradient id="bandFill" x1="0" y1="0" x2="1" y2="0">
          <stop offset="0" stop-color="#6d2a8e"/>
          <stop offset=".5" stop-color="#8a2f96"/>
          <stop offset="1" stop-color="#6a2a8e"/>
        </linearGradient>
      </defs>
      <path d="M0 22 C 300 40, 700 64, 1140 48 L1140 160 L0 160 Z" fill="url(#bandFill)"/>
      <path d="M0 6 C 300 28, 700 50, 1140 36 L1140 48 C 700 64, 300 40, 0 22 Z" fill="var(--silver)"/>
    </svg>

    <div class="brand">
      <span class="brand__dot"></span>
      <span class="brand__name">Brightwell<br>Fitness</span>
    </div>

    <p class="web">brightwellfitness.com</p>
    <p class="fine-print">Some Restrictions Apply</p>

    <div class="badge">
      <svg viewBox="-134 -134 268 268" width="268" height="268" aria-hidden="true">
        <defs>
          <radialGradient id="badgeFill" cx=".4" cy=".3" r=".8">
            <stop offset="0" stop-color="#9ad84f"/>
            <stop offset=".55" stop-color="#3fb540"/>
            <stop offset="1" stop-color="#1d8a38"/>
          </radialGradient>
        </defs>
        <g fill="#ffffff">
          <rect x="-94" y="-94" width="188" height="188" rx="12"/>
          <rect x="-94" y="-94" width="188" height="188" rx="12" transform="rotate(15)"/>
          <rect x="-94" y="-94" width="188" height="188" rx="12" transform="rotate(30)"/>
          <rect x="-94" y="-94" width="188" height="188" rx="12" transform="rotate(45)"/>
          <rect x="-94" y="-94" width="188" height="188" rx="12" transform="rotate(60)"/>
          <rect x="-94" y="-94" width="188" height="188" rx="12" transform="rotate(75)"/>
        </g>
        <g fill="url(#badgeFill)">
          <rect x="-89" y="-89" width="178" height="178" rx="10"/>
          <rect x="-89" y="-89" width="178" height="178" rx="10" transform="rotate(15)"/>
          <rect x="-89" y="-89" width="178" height="178" rx="10" transform="rotate(30)"/>
          <rect x="-89" y="-89" width="178" height="178" rx="10" transform="rotate(45)"/>
          <rect x="-89" y="-89" width="178" height="178" rx="10" transform="rotate(60)"/>
          <rect x="-89" y="-89" width="178" height="178" rx="10" transform="rotate(75)"/>
        </g>
      </svg>
      <div class="badge__text">
        <span class="badge__num">24</span>
        <span class="badge__label">Hour<br>Access</span>
      </div>
    </div>
  </main>
</body>
</html>
```